Hi I need a website for an audio visual company called "Vorne"

We supply and install all types of technology within the very high end London residential market this includes cinemas, distributed audio (music in principle rooms) TVs, WiFi, security (video entry, CCTV, Intruder alarms), Mood lighting (keldax), electric window treatments (curtains and blinds)
similar companies....https://brightmesa.co.uk/#brightmesa
https://www.tarnspool.co.uk/

```html
<!DOCTYPE html>
<html lang="en">
<head>
<meta charset="utf-8">
<title>Vorne — Smart Home Solutions</title>
<link href="https://fonts.googleapis.com/css2?family=Montserrat:wght@400;500;600;700&display=swap" rel="stylesheet">
<style>
:root{
  --ink:#111111;
  --tan:#c0916a;
  --accent:#c8956a;
  --white:#ffffff;
  --dark-text:#1a1a1a;
  --muted:#e6e6e6;
}
*{box-sizing:border-box;margin:0;padding:0}
html,body{width:1200px;height:4071px;overflow:hidden}
body{position:relative;background:var(--ink);font-family:'Montserrat',sans-serif;color:var(--white)}
.abs{position:absolute}
.band{position:absolute;left:0;width:1200px}
.band-dark{background:var(--ink)}
.band-tan{background:var(--tan)}
.logo{display:flex;align-items:center;gap:14px;font-weight:400;font-size:40px;letter-spacing:12px;color:var(--white)}
.logo-mark{width:34px;height:34px;background:var(--tan)}
.nav{display:flex;font-size:16px;font-weight:600}
.nav a{color:var(--white);text-decoration:none;position:absolute;white-space:nowrap}
.nav a.is-active{color:var(--accent)}
.hero-title{font-size:39px;font-weight:600;line-height:47px}
.hero-title .gold{color:var(--accent)}
.hero-copy{font-size:12.5px;line-height:21px;width:430px}
.btn{position:absolute;display:flex;align-items:center;justify-content:center;border:2px solid var(--accent);border-radius:30px;font-size:16px;color:var(--white);text-decoration:none}
.btn-dark{border-color:var(--dark-text);color:var(--dark-text)}
.photo{position:absolute}
.section-title{font-size:39px;font-weight:600;letter-spacing:1px}
.rule{position:absolute;height:3px;background:var(--accent)}
.rule-dark{background:var(--dark-text)}
.body-copy{font-size:17.5px;line-height:30px;width:500px}
.about-copy{color:var(--dark-text)}
.service-title{font-size:39px;font-weight:600;letter-spacing:1px}
.center{left:0;width:1200px;text-align:center}
.quote{font-size:19px;font-weight:500;line-height:33px;color:var(--dark-text);text-align:center}
.quote-name{font-size:27px;font-weight:500;color:var(--dark-text)}
.arrow{position:absolute;width:50px;height:50px}
.news-title{font-size:25px;font-weight:600}
.news-input{position:absolute;background:var(--white);border-radius:30px;color:var(--dark-text);font-size:13px;font-weight:500;display:flex;align-items:center;padding-left:22px}
.news-send{position:absolute;background:var(--tan);border-radius:30px;color:var(--dark-text);font-size:20px;font-weight:600;display:flex;align-items:center;justify-content:center}
.foot-nav a{position:absolute;color:var(--white);text-decoration:none;font-size:19px;font-weight:600;white-space:nowrap}
.copyright{font-size:17px;font-weight:500}
</style>
</head>
<body>

<!-- Header + hero -->
<section class="band band-dark" style="top:0;height:553px">
  <div class="logo abs" style="left:98px;top:44px"><span class="logo-mark"></span>VORNE</div>
  <nav class="nav">
    <a class="is-active" href="#" style="left:571px;top:55px">HOME</a>
    <a href="#" style="left:677px;top:55px">ABOUT US</a>
    <a href="#" style="left:817px;top:55px">OUR SERVICES</a>
    <a href="#" style="left:996px;top:55px">CONTACT US</a>
  </nav>
  <h1 class="hero-title abs" style="left:98px;top:195px">SMART<br><span class="gold">HOME SOLUTIONS</span></h1>
  <p class="hero-copy abs" style="left:100px;top:298px">Lorem ipsum dolor sit amet, consectetur adipiscing elit, sed do eiusmod tempor incididunt ut labore et dolore magna aliqua. Ut enim ad minim veniam, quis nostrud</p>
  <a class="btn" href="#" style="left:98px;top:378px;width:180px;height:46px">GET STARTED</a>
  <div class="photo" role="img" aria-label="Man with headphones at a studio microphone and mixing desk" style="left:568px;top:104px;width:591px;height:388px;background:linear-gradient(120deg,#0f5a63 0%,#1d2a3a 45%,#5a2b3a 75%,#8a3aa8 100%)"></div>
</section>

<!-- About -->
<section class="band band-tan" style="top:553px;height:674px">
  <div class="photo" role="img" aria-label="Technician installing an alarm panel on a white brick wall" style="left:73px;top:57px;width:441px;height:566px;background:linear-gradient(90deg,#e9e9e6 0%,#cfd2d6 45%,#8fa3bd 100%)"></div>
  <h2 class="section-title abs" style="left:596px;top:68px;color:var(--dark-text)">ABOUT US</h2>
  <div class="rule rule-dark" style="left:596px;top:121px;width:103px"></div>
  <p class="body-copy about-copy abs" style="left:596px;top:140px">Sed ut perspiciatis unde omnis iste natus error sit voluptatem accusantium doloremque laudantium, totam rem aperiam, eaque ipsa quae ab illo inventore veritatis et quasi architecto beatae vitae dicta sunt explicabo. Nemo enim ipsam voluptatem quia voluptas sit aspernatur aut odit aut fugit, sed quia consequuntur magni dolores eos qui ratione voluptatem sequi nesciunt. Neque porro quisquam est, qui dolorem ipsum quia dolor sit amet, consectetur, adipisci velit</p>
  <p class="body-copy about-copy abs" style="left:596px;top:422px">Sed ut perspiciatis unde omnis iste natus error sit voluptatem accusantium doloremque laudantium, totam rem aperiam, eaque ipsa</p>
  <a class="btn btn-dark" href="#" style="left:598px;top:530px;width:180px;height:46px">READ MORE</a>
</section>

<!-- Services -->
<section class="band band-dark" style="top:1227px;height:1998px">
  <h2 class="section-title abs center" style="top:98px">OUR SERVICES</h2>
  <div class="rule" style="left:549px;top:166px;width:101px"></div>

  <h3 class="service-title abs" style="left:96px;top:272px">CINEMAS</h3>
  <p class="body-copy abs" style="left:96px;top:343px;color:var(--muted)">Sed ut perspiciatis unde omnis iste natus error sit voluptatem accusantium doloremque laudantium, totam rem aperiam, eaque ipsa quae ab illo inventore veritatis et quasi architecto beatae vitae dicta sunt explicabo. Nemo enim ipsam voluptatem quia voluptas sit aspernatur aut odit aut fugit, sed quia consequuntur magni dolores eos qui ratione voluptatem sequi nesciunt. Neque porro quisquam est, qui dolorem ipsum quia dolor sit amet, consectetur, adipisci velit</p>
  <a class="btn" href="#" style="left:98px;top:645px;width:180px;height:46px">VIEW MORE</a>
  <div class="photo" role="img" aria-label="Couple in 3D glasses laughing in a cinema with drinks" style="left:664px;top:245px;width:440px;height:463px;background:linear-gradient(160deg,#6a3a2e 0%,#3a2a26 40%,#c9c2bb 70%,#b32a25 100%)"></div>

  <div class="photo" role="img" aria-label="Audio mixing console with illuminated faders and laptops" style="left:96px;top:793px;width:440px;height:464px;background:linear-gradient(135deg,#2a2a2e 0%,#1a1a1c 40%,#3a2a40 70%,#141414 100%)"></div>
  <h3 class="service-title abs" style="left:598px;top:814px">DISTRIBUTED AUDIO</h3>
  <p class="body-copy abs" style="left:598px;top:885px;color:var(--muted)">Sed ut perspiciatis unde omnis iste natus error sit voluptatem accusantium doloremque laudantium, totam rem aperiam, eaque ipsa quae ab illo inventore veritatis et quasi architecto beatae vitae dicta sunt explicabo. Nemo enim ipsam voluptatem quia voluptas sit aspernatur aut odit aut fugit, sed quia consequuntur magni dolores eos qui ratione voluptatem sequi nesciunt. Neque porro quisquam est, qui dolorem ipsum quia dolor sit amet, consectetur, adipisci velit</p>
  <a class="btn" href="#" style="left:599px;top:1187px;width:180px;height:46px">VIEW MORE</a>

  <h3 class="service-title abs" style="left:108px;top:1354px">TVs</h3>
  <p class="body-copy abs" style="left:96px;top:1426px;color:var(--muted)">Sed ut perspiciatis unde omnis iste natus error sit voluptatem accusantium doloremque laudantium, totam rem aperiam, eaque ipsa quae ab illo inventore veritatis et quasi architecto beatae vitae dicta sunt explicabo. Nemo enim ipsam voluptatem quia voluptas sit aspernatur aut odit aut fugit, sed quia consequuntur magni dolores eos qui ratione voluptatem sequi nesciunt. Neque porro quisquam est, qui dolorem ipsum quia dolor sit amet, consectetur, adipisci velit</p>
  <a class="btn" href="#" style="left:98px;top:1728px;width:180px;height:46px">VIEW MORE</a>
  <div class="photo" role="img" aria-label="Wall-mounted TV showing a football match in a dark living room" style="left:664px;top:1326px;width:440px;height:464px;background:radial-gradient(ellipse at 50% 40%,#4f7d3a 0%,#2b3f5a 35%,#1f2a44 65%,#3a2c22 100%)"></div>

  <a class="btn" href="#" style="left:484px;top:1872px;width:232px;height:44px;font-size:15px">VIEW ALL SERVICES</a>
</section>

<!-- Testimonials -->
<section class="band band-tan" style="top:3225px;height:429px">
  <h2 class="section-title abs center" style="top:68px;color:var(--dark-text)">OUR TESTIMONIALS</h2>
  <div class="rule rule-dark" style="left:549px;top:132px;width:101px"></div>
  <svg class="arrow" style="left:46px;top:173px" viewBox="0 0 50 50" aria-label="Previous">
    <circle cx="25" cy="25" r="22.5" fill="none" stroke="#1a1a1a" stroke-width="3"/>
    <path d="M36 25H14M22 17l-8 8 8 8" fill="none" stroke="#1a1a1a" stroke-width="3" stroke-linecap="round" stroke-linejoin="round"/>
  </svg>
  <p class="quote abs" style="left:150px;top:168px;width:900px">Lorem ipsum dolor sit amet, consectetur adipiscing elit, sed do eiusmod tempor incididunt ut labore et dolore magna aliqua. Ut enim ad minim veniam, quis nostrud exercitation ullamco laboris nisi ut aliquip ex ea commodo consequat. Duis aute irure dolor in reprehenderit in voluptate velit esse cillum dolore eu fugiat nulla pariatur.</p>
  <svg class="arrow" style="left:1096px;top:192px" viewBox="0 0 50 50" aria-label="Next">
    <circle cx="25" cy="25" r="22.5" fill="none" stroke="#1a1a1a" stroke-width="3"/>
    <path d="M14 25h22M28 17l8 8-8 8" fill="none" stroke="#1a1a1a" stroke-width="3" stroke-linecap="round" stroke-linejoin="round"/>
  </svg>
  <p class="quote-name abs center" style="top:330px">Marlo Fenn</p>
</section>

<!-- Footer -->
<footer class="band band-dark" style="top:3654px;height:417px">
  <div class="logo abs" style="left:153px;top:106px"><span class="logo-mark"></span>VORNE</div>
  <h4 class="news-title abs" style="left:629px;top:75px">Subscribe to our newsletter</h4>
  <div class="news-input" style="left:628px;top:125px;width:305px;height:53px">Enter Your Email</div>
  <div class="news-send" style="left:945px;top:122px;width:143px;height:58px">Send</div>
  <nav class="foot-nav">
    <a href="#" style="left:275px;top:263px">HOME</a>
    <a href="#" style="left:405px;top:263px">ABOUT US</a>
    <a href="#" style="left:577px;top:263px">OUR SERVICES</a>
    <a href="#" style="left:795px;top:263px">CONTACT US</a>
  </nav>
  <p class="copyright abs center" style="top:337px">Copyright Vorne © 2024. All Rights Reserved.</p>
</footer>

</body>
</html>
```